ARC VOLLEY Business Card Project

I'd like to request a business card design for the new company I've launched.
The name of the company is "ARC VOLLEY" an indoor unmanned tennis practice facility.
We would like to see designs that use our brand identity color in the logo I've attached.
We hope to get the design with modern, luxurious and elegant tone and manner.
We hope the logo should not be too big.

Business card must have elements as below:
- Logo (One of the logos I've attached)
- Name (In Korean Text) : 박 서 윤
- Title (In Korean Text) : 대표
- Phone Number : 010-8472-3916
- Email Address : seoyun.park@arcvolley-example.co.kr
- Website : www.arcvolley-example.co.kr
- Instagram : arcvolley
- Address (In Korean text) : 경기도 용인시 수지구 풍덕천로 456 미래타워 5층 501호, 502호

Target Market(s)

Tennis amateurs in 20 to 40s

Industry/Entity Type

Sports, Hobby

Contact Information for Business Card

- Logo (One of the logos I've attached) - Name (In Korean Text) : 박 서 윤 - Title (In Korean Text) : 대표 - Phone Number : 010-8472-3916 - Email Address : seoyun.park@arcvolley-example.co.kr - Website : www.arcvolley-example.co.kr - Instagram : arcvolley - Address (In Korean text) : 경기도 용인시 수지구 풍덕천로 456 미래타워 5층 501호, 502호

Font styles to use
Sans Serif

Requirements
Must have
• Double sided
Nice to have
• Logo with intaglio or relief embossing
Should not have
• Logo should not be too big.

```html
<!DOCTYPE html>
<html lang="ko">
<head>
<meta charset="utf-8">
<title>ARC VOLLEY Business Card</title>
<link rel="stylesheet" href="https://fonts.googleapis.com/css2?family=Noto+Serif+KR:wght@400;600;700&display=swap">
<style>
  :root {
    --forest: #2d5a36;
    --forest-deep: #234a2b;
    --forest-light: #3f7a4a;
    --ink: #333333;
    --slate: #4a4a4a;
    --paper: #ffffff;
    --backdrop: #1e1e1e;
  }
  * { margin: 0; padding: 0; box-sizing: border-box; }
  html, body { width: 1200px; height: 900px; overflow: hidden; }
  body {
    background: var(--backdrop);
    font-family: "Noto Serif KR", serif;
    position: relative;
  }
  .card {
    position: absolute;
    left: 240px;
    width: 720px;
    height: 400px;
    overflow: hidden;
    box-shadow: 0 10px 30px rgba(0,0,0,.5);
  }
  .card-front { top: 35px; background: var(--paper); }
  .card-back { top: 465px; background: var(--forest); }

  .front-swoosh { position: absolute; inset: 0; }

  .brand {
    position: absolute;
    left: 60px;
    top: 130px;
    width: 290px;
    text-align: center;
  }
  .brand-mark {
    width: 64px; height: 64px;
    border-radius: 50%;
    background: var(--forest);
    margin: 0 auto 14px;
  }
  .brand-name {
    font-size: 34px;
    font-weight: 600;
    letter-spacing: 2px;
    color: var(--forest);
  }
  .divider {
    position: absolute;
    left: 375px; top: 70px;
    width: 2px; height: 190px;
    background: var(--forest);
  }
  .contact {
    position: absolute;
    left: 400px; top: 72px;
    color: var(--ink);
  }
  .contact-name {
    font-size: 26px;
    font-weight: 700;
    letter-spacing: 6px;
    color: var(--forest);
  }
  .contact-title { font-size: 15px; margin-top: 2px; }
  .contact-address {
    font-size: 14.5px;
    line-height: 1.45;
    margin-top: 16px;
  }
  .contact-list { list-style: none; margin-top: 10px; font-size: 14.5px; line-height: 1.6; }
  .contact-list li { display: flex; align-items: center; gap: 7px; }
  .contact-list svg { width: 13px; height: 13px; flex: none; }

  .back-pattern {
    position: absolute; inset: 0;
    background: radial-gradient(circle at 70% 70%, var(--forest-light), var(--forest) 55%, var(--forest-deep));
  }
  .back-brand {
    position: absolute;
    right: 50px; bottom: 60px;
    display: flex; align-items: center; gap: 14px;
  }
  .back-brand-mark {
    width: 46px; height: 46px; border-radius: 50%;
    border: 3px solid var(--paper);
  }
  .back-brand-name {
    font-size: 32px; font-weight: 600; letter-spacing: 2px;
    color: var(--paper);
  }
</style>
</head>
<body>
  <section class="card card-front" aria-label="Card front">
    <svg class="front-swoosh" viewBox="0 0 720 400" preserveAspectRatio="none" aria-hidden="true">
      <path d="M0 235 C 150 300, 400 350, 720 345 L720 400 L0 400 Z" fill="var(--forest)"/>
      <path d="M180 300 C 330 345, 520 360, 720 350 L720 362 C 520 372, 330 360, 180 300 Z" fill="var(--slate)"/>
      <path d="M0 250 C 150 310, 400 356, 720 352" fill="none" stroke="var(--paper)" stroke-width="6"/>
    </svg>

    <div class="brand">
      <div class="brand-mark"></div>
      <div class="brand-name">ARC VOLLEY</div>
    </div>

    <div class="divider"></div>

    <div class="contact">
      <div class="contact-name">박 서 윤</div>
      <div class="contact-title">대표</div>
      <p class="contact-address">경기도 용인시 수지구 풍덕천로<br>456 미래타워 5층 501호, 502호</p>
      <ul class="contact-list">
        <li>
          <svg viewBox="0 0 16 16"><path d="M3 1h3l1.5 4-2 1.5a9 9 0 0 0 4 4L11 8.5l4 1.5v3a2 2 0 0 1-2 2A12 12 0 0 1 1 3a2 2 0 0 1 2-2z" fill="var(--forest)"/></svg>
          010-8472-3916
        </li>
        <li>
          <svg viewBox="0 0 16 16"><rect x="1" y="3" width="14" height="10" rx="1" fill="var(--forest)"/><path d="M1 4l7 5 7-5" fill="none" stroke="var(--paper)" stroke-width="1.3"/></svg>
          seoyun.park@arcvolley-example.co.kr
        </li>
        <li>
          <svg viewBox="0 0 16 16"><circle cx="8" cy="8" r="7" fill="var(--forest)"/><path d="M1 8h14M8 1c3 3 3 11 0 14M8 1c-3 3-3 11 0 14" fill="none" stroke="var(--paper)" stroke-width="1"/></svg>
          www.arcvolley-example.co.kr
        </li>
        <li>
          <svg viewBox="0 0 16 16"><rect x="1.5" y="1.5" width="13" height="13" rx="3.5" fill="none" stroke="var(--forest)" stroke-width="1.8"/></svg>
          arcvolley
        </li>
      </ul>
    </div>
  </section>

  <section class="card card-back" aria-label="Card back">
    <div class="back-pattern" role="img" aria-label="Embossed repeating brand-mark pattern in tones of green"></div>
    <div class="back-brand">
      <div class="back-brand-mark"></div>
      <div class="back-brand-name">ARC VOLLEY</div>
    </div>
  </section>
</body>
</html>
```